A 3d printing services company "The Velvet Lattice" needs a clutter breaking business card design

The Velvet Lattice is a 3d design, animation and printing services company. We are in the B2B and B2C space. www.velvetlattice.com.sg
We have been in business for a year.
The logo is already done (the current file is attached).
We need a business card design which reflects the 3d printing and animations services of the company. A standard rectangular shape is not an option. The card can be die cut.
The card should have the colors of the logo and should have a high tech wow feel to it.
The front of the card should have my name, designation, cellphone email and website details. No need for an office address.
Name: Raghavan Kulkarni
Designation: Founder Director
Cellphone (65)91827345
email: raghavan@velvetlattice.com.sg
website: www.velvetlattice.com.sg
The back of the card should have the services we offer:
1. 3d Design and Modelling
2. 3d Animation
3. 3D Printing
The tag line is: "make your ideas real"
Am uploading the current business card files(back and front).
Target Market(s)
Business owners and C level managers in Marine, Healthcare industry
Industry/Entity Type
Printing
Contact Information for Business Card
Name: Raghavan Kulkarni
Cellphone (65)91827345
2. 3d Animation
3. 3D Printing

```html
<!DOCTYPE html>
<html lang="en">
<head>
<meta charset="utf-8">
<title>The Velvet Lattice – Business Card</title>
<link rel="stylesheet" href="https://fonts.googleapis.com/css2?family=Exo+2:wght@400;500;700&display=swap">
<style>
  :root {
    --page-bg: #dfe2e4;
    --card-top: #f8f9f9;
    --card-mid: #f0f2f3;
    --card-low: #e7eaeb;
    --card-edge: #c6cbce;
    --ink: #34373a;
    --title-blue: #2d3f9e;
    --brand-green: #3cb54a;
    --brand-blue: #1f56b8;
    --band-dark: #2a3f9c;
    --band-cyan: #19b3e8;
    --rule: #8c9095;
    --white: #ffffff;
  }
  * { margin: 0; padding: 0; box-sizing: border-box; }
  html, body {
    width: 1200px; height: 768px; overflow: hidden;
    background: var(--page-bg);
    font-family: "Exo 2", sans-serif;
  }
  .card {
    position: absolute; left: 100px; top: 93px;
    width: 1000px; height: 581px;
    background: linear-gradient(160deg, var(--card-top) 0%, var(--card-mid) 60%, var(--card-low) 100%);
    border: 1px solid var(--card-edge);
    border-radius: 34px;
    overflow: hidden;
    box-shadow: 0 12px 40px rgba(0,0,0,0.12);
    color: var(--ink);
  }
  .brand {
    position: absolute; right: 48px; top: 62px;
    display: flex; align-items: center; gap: 34px;
  }
  .brand-dot {
    width: 190px; height: 190px; border-radius: 50%;
    background: var(--brand-blue);
  }
  .brand-name {
    font-size: 52px; font-weight: 700; line-height: 1.02;
    color: var(--brand-green); text-align: right;
  }
  .person-name {
    position: absolute; left: 41px; top: 190px;
    font-size: 27px; font-weight: 500; letter-spacing: 2px; text-transform: uppercase;
  }
  .person-title {
    position: absolute; left: 41px; top: 240px;
    font-size: 21px; font-weight: 500; color: var(--title-blue); letter-spacing: 0.5px;
  }
  .divider {
    position: absolute; left: 61px; top: 285px; width: 690px; height: 2px;
    background: linear-gradient(90deg, rgba(140,144,149,0.2), var(--rule) 40%, rgba(140,144,149,0.3));
  }
  .address {
    position: absolute; left: 41px; top: 380px;
    font-size: 21px; line-height: 31px; letter-spacing: 0.5px;
  }
  .contacts { list-style: none; }
  .contacts li {
    position: absolute; right: 40px;
    display: flex; align-items: center; justify-content: flex-end; gap: 14px;
    font-size: 21px; letter-spacing: 1px; line-height: 26px; white-space: nowrap;
  }
  .contacts li.small { font-size: 18px; letter-spacing: 0.5px; }
  .contacts .office { top: 312px; }
  .contacts .mobile { top: 361px; }
  .contacts .fax    { top: 407px; }
  .contacts .email  { top: 447px; }
  .contacts .web    { top: 481px; }
  .contacts svg { width: 22px; height: 22px; fill: var(--brand-blue); flex: none; }
  .bands { position: absolute; left: 0; bottom: 0; width: 1000px; height: 64px; }
  .band-web {
    position: absolute; left: 41px; bottom: 20px;
    font-size: 19px; color: var(--white); letter-spacing: 0.5px; font-weight: 500;
  }
</style>
</head>
<body>
  <article class="card">
    <div class="brand">
      <div class="brand-dot"></div>
      <div class="brand-name">The Velvet<br>Lattice</div>
    </div>

    <h1 class="person-name">Raghavan Kulkarni</h1>
    <p class="person-title">Founder Director</p>

    <div class="divider"></div>

    <p class="address">21 Harbourfront Walk #08-14<br>Singapore 098637</p>

    <ul class="contacts">
      <li class="office">(65)62718304
        <svg viewBox="0 0 24 24"><path d="M6.6 10.8a15 15 0 0 0 6.6 6.6l2.2-2.2c.3-.3.7-.4 1-.2 1.1.4 2.3.6 3.6.6.6 0 1 .4 1 1V20c0 .6-.4 1-1 1A17 17 0 0 1 3 4c0-.6.4-1 1-1h3.5c.6 0 1 .4 1 1 0 1.3.2 2.5.6 3.6.1.3 0 .7-.2 1z"/></svg>
      </li>
      <li class="mobile">(65)91827345
        <svg viewBox="0 0 24 24"><path d="M7 1h10a2 2 0 0 1 2 2v18a2 2 0 0 1-2 2H7a2 2 0 0 1-2-2V3a2 2 0 0 1 2-2zm0 3v15h10V4zm5 16.2a.9.9 0 1 0 0 1.8.9.9 0 0 0 0-1.8z"/></svg>
      </li>
      <li class="fax">(65)62718305
        <svg viewBox="0 0 24 24"><path d="M5 8h3V2h10v6h1a3 3 0 0 1 3 3v9a2 2 0 0 1-2 2H5a3 3 0 0 1-3-3v-8a3 3 0 0 1 3-3zm5-4v4h6V4zm1 8v2h2v-2zm4 0v2h2v-2zm-4 4v2h2v-2zm4 0v2h2v-2zM3 11v8h3v-8z"/></svg>
      </li>
      <li class="email small">raghavan@velvetlattice.com.sg
        <svg viewBox="0 0 24 24"><path d="M2 5h20v14H2zm2 2v.4l8 5.2 8-5.2V7zm0 2.8V17h16V9.8l-8 5.2z"/></svg>
      </li>
      <li class="web small">www.velvetlattice.com.sg
        <svg viewBox="0 0 24 24"><path d="M12 2a10 10 0 1 0 0 20 10 10 0 0 0 0-20zm6.9 6h-3a15 15 0 0 0-1.3-3.9A8 8 0 0 1 18.9 8zM12 4c.8 1.2 1.5 2.5 1.9 4h-3.8c.4-1.5 1.1-2.8 1.9-4zM4.3 14a8 8 0 0 1 0-4h3.4a16 16 0 0 0 0 4zm.8 2h3a15 15 0 0 0 1.3 3.9A8 8 0 0 1 5.1 16zm3-8h-3a8 8 0 0 1 4.3-3.9C8.8 5.3 8.4 6.6 8.1 8zM12 20c-.8-1.2-1.5-2.5-1.9-4h3.8c-.4 1.5-1.1 2.8-1.9 4zm2.3-6H9.7a14 14 0 0 1 0-4h4.6a14 14 0 0 1 0 4zm.3 5.9c.6-1.2 1-2.5 1.3-3.9h3a8 8 0 0 1-4.3 3.9zm1.7-5.9a16 16 0 0 0 0-4h3.4a8 8 0 0 1 0 4z"/></svg>
      </li>
    </ul>

    <svg class="bands" viewBox="0 0 1000 64" preserveAspectRatio="none" aria-hidden="true">
      <defs>
        <linearGradient id="bandBlue" x1="0" x2="1" y1="0" y2="0">
          <stop offset="0" stop-color="var(--band-dark)"/>
          <stop offset="0.55" stop-color="var(--band-cyan)"/>
          <stop offset="1" stop-color="var(--brand-blue)"/>
        </linearGradient>
        <linearGradient id="bandGreen" x1="0" x2="1" y1="0" y2="1">
          <stop offset="0" stop-color="#4cc24f"/>
          <stop offset="1" stop-color="#2f9e45"/>
        </linearGradient>
      </defs>
      <path d="M395 18 H1000 V64 H412 C420 46 410 28 395 18 Z" fill="url(#bandBlue)"/>
      <path d="M395 18 H1000" stroke="#ffffff" stroke-width="2" opacity="0.8"/>
      <path d="M0 0 H375 C392 2 402 12 408 26 C414 40 414 54 420 64 H0 Z" fill="url(#bandGreen)"/>
    </svg>
    <span class="band-web">www.velvetlattice.com.sg</span>
  </article>
</body>
</html>
```